Income Tax Flyer - Updates Needed

Just need to update this flyer design and give it a new look. We would like to keep all the same wording but make it stand out a little more. Our selling point is the "Same Day Tax Advance up to $6,000"

Industry/Entity Type

Lending, Small Loans, Tax Services, Title Loans, Personal Loans

```html
<!DOCTYPE html>
<html lang="en">
<head>
<meta charset="utf-8">
<title>Northgate Financial Group – Same Day Tax Advance</title>
<link href="https://fonts.googleapis.com/css2?family=Oswald:wght@500;600&family=Poppins:wght@400;600&display=swap" rel="stylesheet">
<style>
  :root {
    --green: #0f4f2b;
    --green-dark: #0b3f22;
    --red: #c41f2a;
    --white: #ffffff;
    --ink: #1d1d1d;
  }
  * { margin: 0; padding: 0; box-sizing: border-box; }
  html, body { width: 927px; height: 1200px; overflow: hidden; background: var(--white); }
  .flyer { position: relative; width: 927px; height: 1200px; overflow: hidden; background: var(--white); font-family: "Poppins", sans-serif; }
  .shapes { position: absolute; inset: 0; }
  .brand { position: absolute; top: 62px; right: 32px; text-align: right; color: var(--green); font-family: "Poppins", sans-serif; font-weight: 600; }
  .brand-name { font-size: 40px; line-height: 1; }
  .brand-sub { font-size: 11px; letter-spacing: 4px; text-transform: uppercase; margin-top: 6px; }
  .hero-text { position: absolute; left: 29px; top: 345px; width: 364px; text-align: center; color: var(--white); font-family: "Oswald", sans-serif; font-weight: 600; font-size: 47px; line-height: 57px; letter-spacing: 0.5px; }
  .headline { position: absolute; left: 41px; top: 655px; font-family: "Oswald", sans-serif; font-weight: 600; font-size: 43px; line-height: 46px; color: var(--ink); letter-spacing: 0.5px; }
  .features { position: absolute; left: 41px; top: 770px; list-style: none; }
  .feature { display: flex; align-items: center; height: 60px; margin-bottom: 12.5px; }
  .feature-icon { width: 60px; height: 60px; border: 1.5px solid var(--green); border-radius: 50%; display: flex; align-items: center; justify-content: center; }
  .feature-label { margin-left: 27px; color: var(--green); font-weight: 600; font-size: 20.5px; letter-spacing: 0.4px; }
  .offer-text { position: absolute; left: 592px; top: 748px; width: 320px; text-align: center; color: var(--white); font-family: "Oswald", sans-serif; font-weight: 600; font-size: 50px; line-height: 56px; }
  .footer { position: absolute; left: 0; top: 1070px; width: 927px; color: var(--white); }
  .contact-phone { position: absolute; left: 38px; top: 0; }
  .contact-phone .phone-icon { position: absolute; left: 0; top: 8px; }
  .contact-block { position: absolute; }
  .block-title { font-family: "Oswald", sans-serif; font-weight: 500; font-size: 21px; line-height: 1; letter-spacing: 0.5px; }
  .phone-number { font-family: "Oswald", sans-serif; font-weight: 500; font-size: 37px; line-height: 1; margin-top: 12px; letter-spacing: 1px; }
  .block-text { font-size: 15px; line-height: 24.5px; letter-spacing: 0.3px; }
  .call { left: 95px; top: 5px; }
  .call .block-text { margin-top: 11px; }
  .address { left: 385px; top: 5px; }
  .address .block-text { margin-top: 10px; }
  .email { left: 687px; top: 15px; }
  .email .block-text { margin-top: 10px; }
  .social { display: flex; gap: 14px; margin-top: 14px; }
  .social span { width: 17px; height: 17px; border-radius: 50%; background: var(--white); display: block; }
</style>
</head>
<body>
<div class="flyer">
  <svg class="shapes" width="927" height="1200" viewBox="0 0 927 1200" aria-hidden="false">
    <defs>
      <linearGradient id="officeTone" x1="0" y1="0" x2="1" y2="1">
        <stop offset="0" stop-color="#5a4636"/>
        <stop offset="0.45" stop-color="#8fa3b8"/>
        <stop offset="1" stop-color="#e4e8ea"/>
      </linearGradient>
      <linearGradient id="deskTone" x1="0" y1="0" x2="1" y2="1">
        <stop offset="0" stop-color="#3b3a3c"/>
        <stop offset="1" stop-color="#1c1d22"/>
      </linearGradient>
      <filter id="soft" x="-20%" y="-20%" width="140%" height="140%">
        <feDropShadow dx="0" dy="4" stdDeviation="6" flood-opacity="0.25"/>
      </filter>
    </defs>

    <g role="img" aria-label="Photo of a financial advisor reviewing paperwork with a client in a bright office">
      <path d="M0 0 H927 V436 Q330 610 0 487 Z" fill="url(#officeTone)"/>
    </g>
    <path class="swoosh-top" d="M0 487 Q330 610 927 436 V470 Q340 640 0 505 Z" fill="var(--red)"/>

    <g class="hero-badge">
      <circle cx="211" cy="440" r="191" fill="var(--white)" filter="url(#soft)"/>
      <circle cx="211" cy="440" r="182" fill="var(--green)"/>
    </g>

    <g class="offer-badge">
      <circle cx="756" cy="895" r="216" fill="var(--green)"/>
      <circle cx="756" cy="895" r="205" fill="var(--white)"/>
      <g role="img" aria-label="Photo of hands working on paperwork at a desk">
        <circle cx="756" cy="895" r="201" fill="url(#deskTone)"/>
      </g>
    </g>

    <path class="swoosh-bottom" d="M0 1000 Q480 1030 927 962 V1200 H0 Z" fill="var(--red)"/>
    <path d="M0 1014 Q480 1044 927 978 V1200 H0 Z" fill="var(--white)"/>
    <path class="footer-band" d="M0 1018 Q480 1048 927 983 V1200 H0 Z" fill="var(--green)"/>
  </svg>

  <div class="brand">
    <div class="brand-name">Northgate</div>
    <div class="brand-sub">Financial Group</div>
  </div>

  <div class="hero-text">SAME DAY<br>TAX ADVANCE UP<br>TO $6,000</div>

  <h1 class="headline">FILE YOUR TAXES AND APPLY<br>FOR AN EASY ADVANCE!</h1>

  <ul class="features">
    <li class="feature">
      <span class="feature-icon">
        <svg width="28" height="28" viewBox="0 0 28 28"><circle cx="14" cy="14" r="11.5" fill="none" stroke="var(--red)" stroke-width="2.5"/><path d="M14 7.5 V14 L18.5 17" fill="none" stroke="var(--red)" stroke-width="2.5" stroke-linecap="round"/></svg>
      </span>
      <span class="feature-label">Available In 24 Hours or Less</span>
    </li>
    <li class="feature">
      <span class="feature-icon">
        <svg width="32" height="22" viewBox="0 0 32 22"><rect x="1.5" y="1.5" width="29" height="19" rx="1.5" fill="none" stroke="var(--red)" stroke-width="2.5"/><rect x="5" y="5" width="22" height="12" fill="var(--red)"/><circle cx="16" cy="11" r="4.5" fill="var(--white)"/></svg>
      </span>
      <span class="feature-label">Choose Your Loan Amount</span>
    </li>
    <li class="feature">
      <span class="feature-icon">
        <svg width="32" height="28" viewBox="0 0 32 28"><ellipse cx="12" cy="10" rx="11" ry="8" fill="var(--red)"/><path d="M5 15 L3 22 L11 17 Z" fill="var(--red)"/><ellipse cx="21" cy="16" rx="9" ry="6.5" fill="var(--red)" stroke="var(--white)" stroke-width="1.5"/><path d="M25 20 L29 26 L21 21 Z" fill="var(--red)"/></svg>
      </span>
      <span class="feature-label">Contact Us Today!</span>
    </li>
  </ul>

  <div class="offer-text">APPLY<br>HERE FOR<br>$5,000-$6,000<br>TODAY!</div>

  <div class="footer">
    <div class="contact-phone">
      <svg class="phone-icon" width="40" height="40" viewBox="0 0 40 40"><path d="M9 6 C5 8 3 12 5 18 C8 26 13 31 19 34 C22 35 24 34 25 32 L21 25 C20 24 19 24 18 25 L16 26 C13 23 11 20 10 17 L12 15 C13 14 13 13 13 12 L10 6 Z" fill="var(--white)"/><path d="M24 8 Q27 11 24 14 M28 5 Q33 11 28 17" fill="none" stroke="var(--white)" stroke-width="2" stroke-linecap="round"/></svg>
    </div>
    <div class="contact-block call">
      <div class="block-title">CONTACT US TODAY!</div>
      <div class="phone-number">(555) 014-2290</div>
      <div class="block-text">www.northgatefg.com</div>
    </div>
    <div class="contact-block address">
      <div class="block-title">ADDRESS</div>
      <div class="block-text">P.O. Box 48120,<br>1180 Juniper Avenue, Fairview,<br>New Mexico 87000</div>
    </div>
    <div class="contact-block email">
      <div class="block-title">EMAIL</div>
      <div class="block-text">hello@northgatefg.com</div>
      <div class="social" aria-label="Social media links"><span></span><span></span><span></span><span></span></div>
    </div>
  </div>
</div>
</body>
</html>
```